依頼詳細
落ち着いたBARのフライヤーの裏面を作成してください。
表面はロゴだけ印刷します(ロゴは添付ファイル参照ください)
ロゴの世界観を壊さないよう願います。
住所から地図を作成してください。
記載項目
1時間3,000円(税別)
延長 2,500円(税別)
スタッフドリンク 500円~
フード各種 500円~

営業時間 20時~LAST
休日 日曜日・祝日(祝日の前日が日曜日の場合、営業します)
尼崎市柳瀬町4-7-15 ルミエビル2F
電話番号(未定)
サイズ
14.8×10(横書)
ページ数
片面
希望イメージ
シンプル 複雑
単色 カラフル
暗い 明るい
日常 高級
遊び心 厳粛
未来的 伝統的
女性的 男性的
希望する色
グレー系
納品ファイル
• 高解像度JPG (.jpg)
• イラストレーター形式 (.ai)
• フォトショップ形式 (.psd)
• PNG形式 (.png)
補足説明

```html
<!DOCTYPE html>
<html lang="ja">
<head>
<meta charset="utf-8">
<title>MAISON SEPT flyer</title>
<link rel="stylesheet" href="https://fonts.googleapis.com/css2?family=Cinzel:wght@500;700&family=Noto+Serif+JP:wght@400;600&display=swap">
<style>
  :root {
    --page: #ffffff;
    --ink-black: #0b0b0b;
    --leather-mid: #2a2a2a;
    --leather-edge: #060606;
    --lace-light: #9a9a9a;
    --lace-dark: #1c1c1c;
    --text-light: #f2f2f2;
    --text-soft: #cfcfcf;
    --map-paper: #d9d9d9;
  }
  * { margin: 0; padding: 0; box-sizing: border-box; }
  html, body { width: 776px; height: 1200px; overflow: hidden; background: var(--page); }
  .sheet { position: relative; width: 776px; height: 1200px; }

  .card { position: absolute; left: 8px; width: 760px; overflow: hidden; background: var(--ink-black); }
  .card--front { top: 8px; height: 510px; }
  .card--back { top: 668px; height: 524px; }

  .leather {
    position: absolute; inset: 0;
    background: radial-gradient(ellipse at 50% 45%, var(--leather-mid) 0%, #171717 55%, var(--leather-edge) 100%);
  }
  .brand-name {
    position: absolute; left: 0; right: 0; top: 232px;
    text-align: center; color: var(--text-light);
    font-family: "Cinzel", serif; font-weight: 500; font-size: 58px; letter-spacing: 6px;
  }

  .lace-band {
    position: absolute; left: 0; top: 0; width: 100%; height: 64px;
    background: linear-gradient(180deg, var(--lace-dark) 0%, #6e6e6e 45%, var(--lace-dark) 100%);
  }
  .lace-field {
    position: absolute; right: 0; top: 64px; width: 380px; bottom: 0;
    background: linear-gradient(90deg, rgba(11,11,11,1) 0%, rgba(90,90,90,0.7) 45%, var(--lace-light) 75%, #5a5a5a 100%);
  }

  .back-title {
    position: absolute; left: 70px; top: 96px; width: 270px;
    padding-bottom: 6px; border-bottom: 2px solid var(--text-light);
    color: var(--text-light); text-align: center;
    font-family: "Cinzel", serif; font-weight: 700; font-size: 34px; letter-spacing: 2px;
  }
  .price-list {
    position: absolute; left: 76px; top: 160px; width: 320px;
    font-family: "Noto Serif JP", serif; font-size: 18px; color: var(--text-light);
    list-style: none;
  }
  .price-list li { display: flex; line-height: 30px; }
  .price-list .item { width: 170px; }

  .shop-info {
    position: absolute; left: 76px; top: 390px;
    font-family: "Noto Serif JP", serif; font-size: 15px; line-height: 24px; color: var(--text-soft);
  }
  .shop-info .row { display: flex; }
  .shop-info .label { width: 76px; }
  .shop-info .note { padding-left: 76px; }

  .map {
    position: absolute; left: 512px; top: 302px; width: 234px; height: 208px;
    background: linear-gradient(135deg, #e4e4e4 0%, var(--map-paper) 60%, #bdbdbd 100%);
  }
</style>
</head>
<body>
<main class="sheet">
  <section class="card card--front" aria-label="フライヤー表面">
    <div class="leather" role="img" aria-label="黒いレザー調の背景テクスチャ"></div>
    <h1 class="brand-name">MAISON SEPT</h1>
  </section>

  <section class="card card--back" aria-label="フライヤー裏面">
    <div class="lace-band" role="img" aria-label="モノクロのレース模様の帯"></div>
    <div class="lace-field" role="img" aria-label="右側に広がるモノクロのレース模様"></div>

    <h2 class="back-title">MAISON SEPT</h2>

    <ul class="price-list">
      <li><span class="item">1時間</span><span class="price">3,000円(税別)</span></li>
      <li><span class="item">延長</span><span class="price">2,500円(税別)</span></li>
      <li><span class="item">スタッフドリンク</span><span class="price">500円～</span></li>
      <li><span class="item">フード各種</span><span class="price">500円～</span></li>
    </ul>

    <div class="shop-info">
      <p class="row"><span class="label">営業時間</span><span>：20時～LAST</span></p>
      <p class="row"><span class="label">休日</span><span>：日曜日・祝日</span></p>
      <p class="note">(祝日の前日が日曜日の場合、営業します)</p>
      <p class="row"><span class="label">電話番号</span><span>：9876-54321</span></p>
      <p>尼崎市柳瀬町4-7-15 ルミエビル2F</p>
    </div>

    <div class="map" role="img" aria-label="店舗周辺の地図（駅と店舗の位置）"></div>
  </section>
</main>
</body>
</html>
```